Small business that sells dolls used in the investigation of sudden infant deaths needs a website de

We need a modern update to our very simple current website. We are a small business that manufactures and sells featureless dolls used in the training and investigation of sudden infant deaths. With our customer base being primarily government organizations we are looking for design that is to the point and functional while also being engaging.
Updates

Target Market(s)

Our target audience are organizations such as government offices and training organizations looking for information about our product. This makes readability and ease-of-use of the design very important.

Number of Pages Required

5+ page

Font styles to use
Serif

Colors

Designer to choose colors to be used in the design.

Requirements
Must have
• Straightforward website focused towards the product being sold. With secondary focus is being how to contact the business and the care and use of the product. The business logo is orange and blue, these colors do not necessarily need to show up in the website design. Darker and muted/contrasting colors would probably be better.
Nice to have
• It would be nice if the website had a professional feel, that is slightly maternal but is not cutesy. Given the nature of our product, we also would like a site that is very respectful for any case that our product might be used in it.

```html
<!DOCTYPE html>
<html lang="en">
<head>
<meta charset="utf-8">
<title>Gentle Form Dolls</title>
<link href="https://fonts.googleapis.com/css2?family=Roboto:wght@300;400;500;700&display=swap" rel="stylesheet">
<style>
:root{
  --bg:#111111;
  --panel:#232323;
  --panel-dark:#151515;
  --text:#ffffff;
  --muted:#d8d8d8;
  --accent:#c2410c;
  --blue:#1e88e5;
  --blue-light:#3ba2f2;
  --icon:#1e88e5;
}
*{margin:0;padding:0;box-sizing:border-box}
html,body{width:1200px;height:3237px;overflow:hidden;background:var(--bg)}
body{position:relative;font-family:'Roboto',sans-serif;color:var(--text)}
.abs{position:absolute}
.brand{left:97px;top:58px;display:flex;align-items:center;gap:12px;font-size:20px;font-weight:500;color:var(--blue-light)}
.brand-dot{width:34px;height:34px;border-radius:50%;background:var(--blue)}
.nav a{position:absolute;top:60px;font-size:12px;color:var(--text);text-decoration:none;text-transform:uppercase;letter-spacing:.3px}
.nav .active{font-weight:700}
.nav .active::after{content:"";position:absolute;left:-4px;right:-4px;top:26px;height:3px;background:var(--accent)}
.hero-text{left:97px;top:195px;width:480px;font-size:30px;font-weight:300;line-height:36px}
.hero-text b{font-weight:700}
.hero-rule{left:97px;top:430px;width:97px;height:3px;background:var(--accent)}
.btn{left:95px;top:468px;width:166px;height:52px;background:linear-gradient(#3ba2f2,#1976d2);color:#fff;font-size:13px;font-weight:700;display:flex;align-items:center;justify-content:center;text-transform:uppercase}
.hero-photo{left:608px;top:232px;width:532px;height:212px;background:radial-gradient(ellipse at 50% 50%,#e6e6e6 0,#bdbdbd 28%,#1a1a1a 55%,#0e0e0e 100%)}
.section-title{left:80px;font-size:34px;font-weight:300;line-height:36px}
.section-title b{display:block;font-weight:700}
.card{top:794px;width:321px;height:475px;background:var(--panel)}
.card .icon{position:absolute;left:110px;top:80px;width:100px;height:162px;border-radius:40px;background:linear-gradient(#3a3a3a,#2d2d2d)}
.card h3{position:absolute;left:30px;top:312px;font-size:26px;font-weight:300;text-transform:uppercase}
.card h3 b{font-weight:700}
.card p{position:absolute;left:30px;top:356px;width:265px;font-size:14px;line-height:16px;color:var(--muted)}
.row{left:0;width:1200px;height:400px}
.row .half{position:absolute;top:0;height:100%}
.num{font-size:56px;font-weight:300}
.row p{font-size:19px;line-height:24px;width:400px;color:var(--text)}
.row p b{font-weight:700}
.contact{display:flex;gap:14px;align-items:flex-start;font-size:19px;line-height:26px;color:var(--muted)}
.contact svg{flex:none;margin-top:3px}
</style>
</head>
<body>

<header>
  <div class="abs brand"><span class="brand-dot"></span>Gentle Form Dolls</div>
  <nav class="nav">
    <a class="active" href="#" style="left:632px">Home</a>
    <a href="#" style="left:770px">About Us</a>
    <a href="#" style="left:915px">Order</a>
    <a href="#" style="left:1055px">Contact Us</a>
  </nav>
</header>

<section class="hero">
  <p class="abs hero-text">Our online store offers <b>weighted dolls</b> that are used by investigators to reenact and photograph scenes of sudden, unexplained infant death.</p>
  <div class="abs hero-rule"></div>
  <a class="abs btn">Visit Store</a>
  <div class="abs hero-photo" role="img" aria-label="Photo of a white featureless weighted doll lying on a dark background"></div>
</section>

<h2 class="abs section-title" style="top:678px">Product<b>Features</b></h2>

<article class="abs card" style="left:80px">
  <div class="icon" role="img" aria-label="Outline icon of a doll with an orange dress"></div>
  <h3><b>Bright</b> Fabric</h3>
  <p>The six or eight pound featureless dolls are made of light-colored fabric or orange high-visibility fabric for photographic purposes</p>
</article>
<article class="abs card" style="left:445px">
  <div class="icon" role="img" aria-label="Outline icon of a doll with a sparkle"></div>
  <h3><b>Easy</b> to Clean</h3>
  <p>The orange fabric may be wiped with a germicidal solution using a damp rag.</p>
</article>
<article class="abs card" style="left:805px">
  <div class="icon" role="img" aria-label="Outline icon of a doll with a marker"></div>
  <h3><b>Writable</b> Surface</h3>
  <p>A permanent marker may be used to mark the front and back or add facial features as desired.</p>
</article>

<h2 class="abs section-title" style="top:1440px">Product<b>Care</b></h2>

<section class="abs row" style="top:1562px;height:404px">
  <div class="half" style="left:0;width:589px;background:var(--panel)">
    <div class="abs num" style="left:90px;top:30px">01</div>
    <p class="abs" style="left:90px;top:130px">The dolls are made of either light colored or orange fabric so they show up well in photographs.&nbsp; Use a permanent marker to indicate the front and back of the doll.&nbsp; Add a face if desired.</p>
  </div>
  <div class="half" role="img" aria-label="Photo of a marked doll resting on a patterned cushion and red blanket" style="left:589px;width:611px;background:linear-gradient(120deg,#4a4258,#7a6a70 40%,#d8d2cc 55%,#8c1e1e 80%,#6a1414)"></div>
</section>

<section class="abs row" style="top:1970px;height:395px">
  <div class="half" role="img" aria-label="Photo of a person holding a doll supporting its body" style="left:0;width:587px;background:linear-gradient(90deg,#8a1a1a,#b32525 30%,#e8e6e2 45%,#6b5a3e 75%,#3b2f22)"></div>
  <div class="half" style="left:587px;width:613px;background:var(--panel-dark)">
    <div class="abs num" style="left:114px;top:100px">02</div>
    <p class="abs" style="left:114px;top:178px">To help keep your doll in good shape, carry it supporting the body.</p>
  </div>
</section>

<section class="abs row" style="top:2369px;height:402px">
  <div class="half" style="left:0;width:585px;background:var(--panel)">
    <div class="abs num" style="left:90px;top:70px">03</div>
    <p class="abs" style="left:90px;top:151px"><b>Do not</b> carry a doll by the arm or leg as damage may occur due to the weight putting stress on the seams and fabric.</p>
  </div>
  <div class="half" role="img" aria-label="Photo of a hand gripping a doll by the arm" style="left:585px;width:606px;background:linear-gradient(120deg,#0d0d0d,#2a2a2a 30%,#e4e4e4 55%,#cfcfcf 80%,#151515)"></div>
</section>

<h2 class="abs section-title" style="top:2876px">Contact<b>Us</b></h2>

<div class="abs contact" style="left:214px;top:2995px">
  <svg width="22" height="22" viewBox="0 0 24 24"><path fill="#1e88e5" d="M6.6 10.8a15.1 15.1 0 0 0 6.6 6.6l2.2-2.2c.3-.3.7-.4 1-.2 1.1.4 2.3.6 3.6.6.6 0 1 .4 1 1V20c0 .6-.4 1-1 1A17 17 0 0 1 3 4c0-.6.4-1 1-1h3.5c.6 0 1 .4 1 1 0 1.3.2 2.5.6 3.6.1.3 0 .7-.2 1z"/></svg>
  <span>(555) 014-2281</span>
</div>
<div class="abs contact" style="left:214px;top:3060px">
  <svg width="22" height="22" viewBox="0 0 24 24"><path fill="#1e88e5" d="M12 2a7 7 0 0 0-7 7c0 5.3 7 13 7 13s7-7.7 7-13a7 7 0 0 0-7-7zm0 9.5A2.5 2.5 0 1 1 12 6.5a2.5 2.5 0 0 1 0 5z"/></svg>
  <span>Gentle Form Dolls<br>48 NW Alder Lane<br>Harbor Point, WA 98000</span>
</div>
<div class="abs contact" style="left:672px;top:2993px">
  <svg width="22" height="22" viewBox="0 0 24 24"><path fill="#1e88e5" d="M3 9l9-6 9 6v11H3zm2 1.2V18h14v-7.8l-7 4.6z"/></svg>
  <span>hello@gentleformdolls.com</span>
</div>
<div class="abs contact" style="left:672px;top:3057px">
  <svg width="22" height="22" viewBox="0 0 24 24"><circle cx="12" cy="12" r="9" fill="none" stroke="#1e88e5" stroke-width="2"/><path d="M12 7v5l3 2" fill="none" stroke="#1e88e5" stroke-width="2" stroke-linecap="round"/></svg>
  <span>8:00 a.m. - 5:00 p.m<br>Pacific Time<br>Monday - Friday</span>
</div>

</body>
</html>
```